3 out of 100 people will get deadly skin cancer - we need a great illustration that shows this!

We put together a prototype image that communicates lifetime skin cancer risk. (see attached). We are looking for illustrators who can take make a new/better/cooler graphic that communicates this idea. It could be as simple as a superior illustration of the graphic we have or illustrators can propose a completely different idea.What should the illustration communicate?U.S. adults have a lifetime risk of developing skin cancer of 1 in 5. But we don't want to show 1 in 5; we want to show that number in a larger group. For example, in the attached illustration we show 20 in 100 people get skin cancer (i.e., 100 beach towels/umbrellas and 20 of them are red). Research has shown that people are more likely to accurately understand numbers like this when you convey them for larger groups (i.e., 20 out of 100 rather than 1 out of 5). U.S. adults also have a lifetime risk of 2.3% of developing the deadliest form of skin cancer (melanoma). In other words, approximately 3 in 100 people will develop melanoma in their lifetime. Ideally, a single image will convey both lifetime skin cancer risk (20 in 100) and melanoma risk (3 in 100). We will award a top three as follows: 1st place = $300, 2nd place = $250, third place = $200. We will also buy any design beyond 3rd place that we like for $100. For example, we purchased 24 designs in our last contest on Artmarketly.This research is supported by funding from the Corvane Institute of Science.

Target Market(s)

The U.S. public; individuals at high risk of developing skin cancer

Industry/Entity Type

Medicine

Colors

Designer to choose colors to be used in the design.

Requirements
Must have
• an original illustration that conveys both lifetime risk of developing skin cancer (20 in 100) and melanoma (3 in 100).
Nice to have
• It can be beach towels and umbrellas, just like our prototype, or the designers can pitch an original idea. Imagery can be realistic or cartoonish (or something in between). It should be illustrations, though. Not edited photos. The image should be in color (no black and white illustrations).
Should not have
• Photos. Clip art. Free vector images.
• We are looking for original illustrations created by the designer.

```html
<!DOCTYPE html>
<html lang="en">
<head>
<meta charset="utf-8">
<title>Skin Cancer – How likely are you to get it?</title>
<link href="https://fonts.googleapis.com/css2?family=Montserrat:wght@500;600;700;800&display=swap" rel="stylesheet">
<style>
:root{
  --brand-red:#c8102e;
  --ink:#1a1a1a;
  --navy:#14195a;
  --mint:#eafaf0;
  --aqua:#6ef0ec;
  --aqua-pale:#e3f8fa;
  --umbrella-blue:#3fb7e6;
  --umbrella-red:#d4111b;
  --umbrella-black:#2b2b2b;
  --white:#ffffff;
}
*{box-sizing:border-box;margin:0;padding:0}
html,body{width:1200px;height:5389px;overflow:hidden;background:var(--white)}
body{font-family:'Montserrat',sans-serif;color:var(--ink);position:relative}
.abs{position:absolute;left:0;width:1200px}

.brand-header{top:95px;height:110px;display:flex;align-items:center;justify-content:center;gap:22px}
.brand-mark{width:54px;height:54px;border-radius:50%;background:var(--brand-red)}
.brand-name{font-weight:800;font-size:46px;color:var(--brand-red);letter-spacing:1px}

.facts{top:250px;height:700px;background:var(--mint)}
.facts-title{top:370px;display:flex;align-items:center;justify-content:center;gap:26px;font-weight:800;font-size:38px}
.ribbon{width:38px;height:62px}
.fact{left:80px;width:1060px;display:flex;align-items:center;gap:44px;font-weight:700;font-size:25px;line-height:1.45}
.fact-icon{width:110px;height:110px;flex:none}
.fact.uv{top:538px}
.fact.sun{top:700px}

.likely{top:900px;height:560px;background:var(--aqua)}
.wave-top{position:absolute;left:0;top:0;width:1200px;height:40px}
.likely-title{top:1062px;text-align:center;font-size:38px;font-weight:700;color:var(--navy)}
.likely-lead{top:1192px;text-align:center;font-size:24px;font-weight:600}
.likely-question{top:1262px;left:130px;width:940px;text-align:center;font-size:24px;font-weight:600;line-height:1.6}
.beach-scene{top:1410px;height:670px;background:linear-gradient(180deg,#6ef0ec 0%,#8fe7e8 25%,#f6deb1 50%,#f0cf98 75%,#9ab57a 100%)}

.legend{top:2150px;height:70px;display:flex;align-items:center;font-size:25px;font-weight:600}
.legend-item{position:absolute;display:flex;align-items:center;gap:16px}
.legend-item svg{width:64px;height:50px}
.legend .l-blue{left:110px;color:var(--umbrella-blue)}
.legend .l-red{left:490px;color:var(--umbrella-red)}
.legend .l-black{left:840px;color:var(--ink)}

.pictograph{top:2290px;left:149px;width:980px;display:grid;grid-template-columns:repeat(10,98px);grid-auto-rows:102px}
.pictograph svg{width:84px;height:66px}
.u{color:var(--umbrella-blue)}
.u.r{color:var(--umbrella-red)}
.u.k{color:var(--umbrella-black)}

.prevent{top:3360px;height:1300px;background:linear-gradient(180deg,var(--aqua-pale),#f3fcfd)}
.prevent-title{top:3440px;text-align:center;font-size:38px;font-weight:700}
.prevent-intro{top:3668px;left:150px;width:900px;text-align:center;font-size:24px;font-weight:600;line-height:1.6}
.tip{left:72px;width:1060px;display:flex;gap:52px}
.tip-icon{width:110px;height:110px;flex:none;border-radius:14px}
.tip h3{font-size:25px;font-weight:700}
.tip p{font-size:24px;font-weight:500;line-height:1.5;margin-top:6px}
.tip.t1{top:3820px}.tip.t2{top:3978px}.tip.t3{top:4132px}.tip.t4{top:4335px}.tip.t5{top:4532px}

.shore{top:4660px;height:490px;background:linear-gradient(180deg,#f3fcfd 0%,#7fe0ea 35%,#3fc1d6 58%,#eaf8f7 66%,#f3dbb0 78%,#f0cf98 100%)}
.brand-footer{top:5200px;height:120px;display:flex;align-items:center;justify-content:center;gap:22px}
.brand-footer .brand-name{font-size:40px}
</style>
</head>
<body>
<svg width="0" height="0" style="position:absolute">
  <symbol id="um" viewBox="0 0 60 48">
    <path d="M3 22 Q30 -8 57 22 Q50 18 44 22 Q37 17 30 22 Q23 17 16 22 Q10 18 3 22Z" fill="currentColor"/>
    <line x1="30" y1="8" x2="40" y2="44" stroke="#555" stroke-width="1.6"/>
    <path d="M10 44 L26 36 L50 36 L56 44" fill="none" stroke="currentColor" stroke-width="3.2" stroke-linejoin="round"/>
    <line x1="14" y1="44" x2="54" y2="44" stroke="currentColor" stroke-width="2"/>
  </symbol>
</svg>

<header class="abs brand-header">
  <span class="brand-mark"></span>
  <span class="brand-name">CORVANE HEALTH</span>
</header>

<section class="abs facts"></section>
<div class="abs facts-title">
  <svg class="ribbon" viewBox="0 0 38 62"><path d="M19 4 C8 4 8 22 19 30 L6 58 M19 4 C30 4 30 22 19 30 L32 58" fill="none" stroke="var(--brand-red)" stroke-width="7" stroke-linecap="round"/></svg>
  <span>SKIN CANCER</span>
</div>
<div class="abs fact uv">
  <svg class="fact-icon" viewBox="0 0 110 110"><g stroke="#f7941d" stroke-width="6" stroke-linecap="round"><line x1="55" y1="6" x2="55" y2="20"/><line x1="55" y1="90" x2="55" y2="104"/><line x1="6" y1="55" x2="20" y2="55"/><line x1="90" y1="55" x2="104" y2="55"/><line x1="20" y1="20" x2="30" y2="30"/><line x1="80" y1="80" x2="90" y2="90"/><line x1="90" y1="20" x2="80" y2="30"/><line x1="20" y1="90" x2="30" y2="80"/></g><circle cx="55" cy="55" r="28" fill="#f7941d"/><text x="55" y="64" text-anchor="middle" font-family="Montserrat,sans-serif" font-weight="800" font-size="24" fill="#fff">UV</text></svg>
  <p>The primary cause ok skin cancer is exposure to Ultraviolet (UV) light from the sun or indoor tanning.</p>
</div>
<div class="abs fact sun">
  <svg class="fact-icon" viewBox="0 0 110 110"><g stroke="#fbb03b" stroke-width="6" stroke-linecap="round"><line x1="55" y1="6" x2="55" y2="20"/><line x1="55" y1="90" x2="55" y2="104"/><line x1="6" y1="55" x2="20" y2="55"/><line x1="90" y1="55" x2="104" y2="55"/><line x1="20" y1="20" x2="30" y2="30"/><line x1="80" y1="80" x2="90" y2="90"/><line x1="90" y1="20" x2="80" y2="30"/><line x1="20" y1="90" x2="30" y2="80"/></g><circle cx="55" cy="55" r="28" fill="#fbb03b"/></svg>
  <p>The greater the total amount of sun exposure over a lifetime, the greater the chance of melanoma.</p>
</div>

<section class="abs likely">
  <svg class="wave-top" viewBox="0 0 1200 40" preserveAspectRatio="none"><path d="M0 0 L0 20 Q150 0 300 20 T600 20 T900 20 T1200 20 L1200 0Z" fill="var(--mint)"/></svg>
</section>
<h2 class="abs likely-title">How likely are you to get skin cancer?</h2>
<p class="abs likely-lead">Let's say 100 people go to the beach.....</p>
<p class="abs likely-question">How many will develop skin cancer in their lifetime? How many will develop melanoma, the deadliest form of skin cancer?</p>
<div class="abs beach-scene" role="img" aria-label="Illustrated beach seen from above with people swimming, sunbathing on towels and relaxing under umbrellas"></div>

<div class="abs legend">
  <div class="legend-item l-blue"><svg class="u"><use href="#um"/></svg>no skin cancer</div>
  <div class="legend-item l-red"><svg class="u r"><use href="#um"/></svg>skin cancer</div>
  <div class="legend-item l-black"><svg class="u k"><use href="#um"/></svg>melanoma</div>
</div>

<div class="abs pictograph" role="img" aria-label="100 beach umbrellas: 20 red for skin cancer, 3 black for melanoma">
<svg class="u"><use href="#um"/></svg><svg class="u r"><use href="#um"/></svg><svg class="u"><use href="#um"/></svg><svg class="u"><use href="#um"/></svg><svg class="u"><use href="#um"/></svg><svg class="u r"><use href="#um"/></svg><svg class="u"><use href="#um"/></svg><svg class="u"><use href="#um"/></svg><svg class="u r"><use href="#um"/></svg><svg class="u"><use href="#um"/></svg>
<svg class="u"><use href="#um"/></svg><svg class="u"><use href="#um"/></svg><svg class="u"><use href="#um"/></svg><svg class="u"><use href="#um"/></svg><svg class="u"><use href="#um"/></svg><svg class="u"><use href="#um"/></svg><svg class="u"><use href="#um"/></svg><svg class="u r"><use href="#um"/></svg><svg class="u"><use href="#um"/></svg><svg class="u"><use href="#um"/></svg>
<svg class="u"><use href="#um"/></svg><svg class="u"><use href="#um"/></svg><svg class="u"><use href="#um"/></svg><svg class="u r"><use href="#um"/></svg><svg class="u"><use href="#um"/></svg><svg class="u"><use href="#um"/></svg><svg class="u"><use href="#um"/></svg><svg class="u"><use href="#um"/></svg><svg class="u"><use href="#um"/></svg><svg class="u r"><use href="#um"/></svg>
<svg class="u"><use href="#um"/></svg><svg class="u"><use href="#um"/></svg><svg class="u k"><use href="#um"/></svg><svg class="u"><use href="#um"/></svg><svg class="u r"><use href="#um"/></svg><svg class="u"><use href="#um"/></svg><svg class="u"><use href="#um"/></svg><svg class="u"><use href="#um"/></svg><svg class="u r"><use href="#um"/></svg><svg class="u"><use href="#um"/></svg>
<svg class="u r"><use href="#um"/></svg><svg class="u"><use href="#um"/></svg><svg class="u"><use href="#um"/></svg><svg class="u"><use href="#um"/></svg><svg class="u"><use href="#um"/></svg><svg class="u r"><use href="#um"/></svg><svg class="u"><use href="#um"/></svg><svg class="u"><use href="#um"/></svg><svg class="u"><use href="#um"/></svg><svg class="u"><use href="#um"/></svg>
<svg class="u"><use href="#um"/></svg><svg class="u r"><use href="#um"/></svg><svg class="u"><use href="#um"/></svg><svg class="u"><use href="#um"/></svg><svg class="u"><use href="#um"/></svg><svg class="u"><use href="#um"/></svg><svg class="u"><use href="#um"/></svg><svg class="u"><use href="#um"/></svg><svg class="u r"><use href="#um"/></svg><svg class="u"><use href="#um"/></svg>
<svg class="u"><use href="#um"/></svg><svg class="u"><use href="#um"/></svg><svg class="u"><use href="#um"/></svg><svg class="u"><use href="#um"/></svg><svg class="u r"><use href="#um"/></svg><svg class="u"><use href="#um"/></svg><svg class="u"><use href="#um"/></svg><svg class="u k"><use href="#um"/></svg><svg class="u"><use href="#um"/></svg><svg class="u"><use href="#um"/></svg>
<svg class="u"><use href="#um"/></svg><svg class="u r"><use href="#um"/></svg><svg class="u"><use href="#um"/></svg><svg class="u"><use href="#um"/></svg><svg class="u r"><use href="#um"/></svg><svg class="u"><use href="#um"/></svg><svg class="u"><use href="#um"/></svg><svg class="u"><use href="#um"/></svg><svg class="u r"><use href="#um"/></svg><svg class="u"><use href="#um"/></svg>
<svg class="u"><use href="#um"/></svg><svg class="u"><use href="#um"/></svg><svg class="u k"><use href="#um"/></svg><svg class="u"><use href="#um"/></svg><svg class="u"><use href="#um"/></svg><svg class="u"><use href="#um"/></svg><svg class="u r"><use href="#um"/></svg><svg class="u"><use href="#um"/></svg><svg class="u"><use href="#um"/></svg><svg class="u"><use href="#um"/></svg>
<svg class="u"><use href="#um"/></svg><svg class="u"><use href="#um"/></svg><svg class="u r"><use href="#um"/></svg><svg class="u"><use href="#um"/></svg><svg class="u"><use href="#um"/></svg><svg class="u"><use href="#um"/></svg><svg class="u r"><use href="#um"/></svg><svg class="u"><use href="#um"/></svg><svg class="u"><use href="#um"/></svg><svg class="u r"><use href="#um"/></svg>
</div>

<section class="abs prevent"></section>
<h2 class="abs prevent-title">What can you do to prevent skin cancer?</h2>
<p class="abs prevent-intro">Leading medical experts, including those at Halvern Clinic, make these recommendations for preventing skin cancer:</p>
<div class="abs tip t1"><div class="tip-icon" role="img" aria-label="Sun behind a cloud icon" style="background:#fcd27a"></div><div><h3>Avoid the sun from 10 a.m. to 4 p.m.</h3><p>These are the peak hours of sun strength in North America - even in winter and on cloudy days.</p></div></div>
<div class="abs tip t2"><div class="tip-icon" role="img" aria-label="Sunscreen bottle icon" style="background:#9fd9ee"></div><div><h3>Wear sunscreen</h3><p>Reapply sunscreen every two hours or more frequently if you're swimming or sweating.</p></div></div>
<div class="abs tip t3"><div class="tip-icon" role="img" aria-label="Wide brimmed sun hat icon" style="background:#8fe3e8"></div><div><h3>Wear protective clothing</h3><p>Hats wide wide brims and clothing that covers your arms and legs are helpful. Sunscreen doesn't block all UV rays, which cause skin cancer.</p></div></div>
<div class="abs tip t4"><div class="tip-icon" role="img" aria-label="Tanning bed icon" style="background:#c9c9b8"></div><div><h3>Avoid tanning beds</h3><p>Tanning beds operate with UV lights, damaging your skin and potentially leading to cancer.</p></div></div>
<div class="abs tip t5"><div class="tip-icon" role="img" aria-label="Body outline with spots icon" style="background:#f5c08a"></div><div><h3>Self-check your skin</h3><p>If you notice differences, talk with your health care team.</p></div></div>

<div class="abs shore" role="img" aria-label="Illustrated shoreline with waves, sand, shells and a starfish"></div>

<footer class="abs brand-footer">
  <span class="brand-mark"></span>
  <span class="brand-name">CORVANE INSTITUTE OF SCIENCE</span>
</footer>
</body>
</html>
```